Bref créative
Owl Creek Homes
OwlCreekHomes.com
Professional
Dale Pruitt, HOMEAGENT®
2814 Merrow Lane, Suite 207
Austin, TX 78799
Dale@OwlCreekHomes.com
The LOGO "OwlCreekHomes" has been uploaded, and is downloadable, along with the other logos needed for the back side of the card. If needed, change font of slogan "Guiding Austin to Quality Homesteads" slogan.
One idea - 1/2 half of the bat on the front side of the card, with the other half of the bat on the back side of the card, however, that is just an idea and I'm open to any ideas.
The Back Side, i need the 3 logos found in the uploaded material, each with two different formats. Please let me know if you need a different format.
1)" R" - for Homeagent
2)" PLX"
3) the "HOUSE" - equal housing
and add also
4) "Velmont Partners, REALTORS®"
All 4 should be small and located in the same area and/or on the same side of the card.
Owl Creek Homes LOGO
Owl Creek Homes LOGO COLOR
Owl Creek Homes LOGO Black on White
Owl Creek Homes LOGO White on Black
Owl Creek Homes White on Black

```html
<!DOCTYPE html>
<html lang="en">
<head>
<meta charset="utf-8">
<title>Owl Creek Homes – Identity Set</title>
<link rel="stylesheet" href="https://fonts.googleapis.com/css2?family=Michroma&family=Cinzel:wght@400;600&family=Arimo:wght@400;700&display=swap">
<style>
  :root {
    --blue: #1a8ad6;
    --blue-deep: #0b5ea8;
    --blue-pale: #d8ecfa;
    --ink: #1d3c6e;
    --paper: #ffffff;
    --shadow: rgba(0,0,0,0.18);
    --slate-light: #7d7d7d;
    --slate-dark: #2b2b2b;
    --badge: rgba(255,255,255,0.22);
  }
  html, body { margin: 0; padding: 0; overflow: hidden; }
  body { width: 1200px; height: 895px; background: var(--paper); position: relative; font-family: "Arimo", Arial, sans-serif; }

  address { font-style: normal; }
  .brand-name { font-family: "Michroma", sans-serif; color: var(--blue-deep); letter-spacing: 0.5px; white-space: nowrap; }
  .brand-slogan { font-family: "Cinzel", serif; color: var(--blue); white-space: nowrap; }

  /* Primary logo lockup */
  .logo-lockup { position: absolute; left: 76px; top: 440px; width: 390px; text-align: center; }
  .logo-lockup .brand-name { font-size: 25px; }
  .logo-lockup .brand-slogan { font-size: 14px; margin-top: 10px; }

  /* Letterhead */
  .letterhead { position: absolute; left: 516px; top: 36px; width: 480px; height: 648px; background: var(--paper); box-shadow: 0 2px 8px var(--shadow); overflow: hidden; }
  .letterhead .band-top { position: absolute; left: 0; top: 0; width: 100%; height: 22px; background: linear-gradient(90deg, var(--blue-deep), var(--blue) 60%, var(--blue-deep)); }
  .letterhead .band-bottom { position: absolute; left: 0; bottom: 48px; width: 100%; height: 14px; background: linear-gradient(90deg, var(--blue-deep), var(--blue) 60%, var(--blue-deep)); }
  .letterhead .contact { position: absolute; left: 300px; top: 28px; font-size: 7.5px; line-height: 1.25; color: var(--ink); }
  .letterhead .contact .firm { font-size: 10px; font-weight: 700; color: var(--blue-deep); }
  .letterhead .watermark { position: absolute; left: 0; width: 100%; top: 300px; text-align: center; }
  .letterhead .watermark .brand-name { font-size: 26px; color: var(--blue-pale); }
  .letterhead .footer-mark { position: absolute; left: 0; width: 100%; bottom: 82px; text-align: center; }
  .letterhead .footer-mark .brand-name { font-size: 8px; }

  /* Business cards */
  .card { position: absolute; top: 643px; width: 340px; height: 216px; border-radius: 10px; overflow: hidden; box-shadow: 0 2px 8px var(--shadow); }
  .card-front { left: 456px; background: var(--paper); }
  .card-front .band-top { position: absolute; left: 0; top: 0; width: 100%; height: 16px; background: linear-gradient(90deg, var(--blue-deep), var(--blue)); }
  .card-front .swoosh { position: absolute; left: 0; bottom: 0; width: 100%; height: 70px; }
  .card-front .mark { position: absolute; left: 10px; top: 90px; width: 162px; text-align: center; }
  .card-front .mark .brand-name { font-size: 10px; }
  .card-front .mark .brand-slogan { font-size: 5.6px; margin-top: 5px; }
  .card-front .divider { position: absolute; left: 180px; top: 58px; width: 1px; height: 78px; background: var(--blue); }
  .card-front .contact { position: absolute; left: 190px; top: 60px; font-size: 8px; line-height: 1.3; color: var(--ink); }
  .card-front .contact .firm { font-size: 11px; font-weight: 700; color: var(--blue-deep); }

  .card-back { left: 821px; background: radial-gradient(ellipse at 50% 45%, var(--slate-light), var(--slate-dark) 85%); }
  .card-back .mark { position: absolute; left: 0; width: 100%; top: 92px; text-align: center; }
  .card-back .mark .brand-name { font-size: 18px; color: #cfcfcf; }
  .card-back .url { position: absolute; left: 0; width: 100%; bottom: 20px; text-align: center; font-size: 8px; font-weight: 700; color: #e6e6e6; }
  .card-back .badges { position: absolute; right: 14px; bottom: 16px; display: flex; gap: 4px; }
  .card-back .badge { width: 12px; height: 12px; border-radius: 2px; background: var(--badge); }
</style>
</head>
<body>

  <section class="logo-lockup">
    <div class="brand-name">OWL CREEK HOMES</div>
    <div class="brand-slogan">Guiding Austin to Quality Homesteads</div>
  </section>

  <section class="letterhead">
    <div class="band-top"></div>
    <address class="contact">
      <div class="firm">Owl Creek Homes</div>
      Dale Pruitt, HOMEAGENT®<br>
      2814 Merrow Lane, Suite 207<br>
      Austin, TX 78799<br>
      P: 512.555.0147<br>
      Dale@OwlCreekHomes.com
    </address>
    <div class="watermark"><span class="brand-name">OWL CREEK HOMES</span></div>
    <div class="footer-mark"><span class="brand-name">OWL CREEK HOMES</span></div>
    <div class="band-bottom"></div>
  </section>

  <section class="card card-front">
    <div class="band-top"></div>
    <div class="mark">
      <div class="brand-name">OWL CREEK HOMES</div>
      <div class="brand-slogan">Guiding Austin to Quality Homesteads</div>
    </div>
    <div class="divider"></div>
    <address class="contact">
      <div class="firm">Owl Creek Homes</div>
      Dale Pruitt, HOMEAGENT®<br>
      2814 Merrow Lane, Suite 207<br>
      Austin, TX 78799<br>
      P: 512.555.0147<br>
      Dale@OwlCreekHomes.com
    </address>
    <svg class="swoosh" viewBox="0 0 340 70" preserveAspectRatio="none" aria-hidden="true">
      <path d="M0 30 C90 70 220 10 340 38 L340 70 L0 70 Z" fill="var(--blue-deep)"/>
      <path d="M0 42 C100 78 230 22 340 48 L340 70 L0 70 Z" fill="var(--blue)"/>
    </svg>
  </section>

  <section class="card card-back">
    <div class="mark"><span class="brand-name">OWL CREEK HOMES</span></div>
    <div class="url">OwlCreekHomes.com</div>
    <div class="badges" role="img" aria-label="Membership and equal housing badges">
      <span class="badge"></span><span class="badge"></span><span class="badge"></span><span class="badge"></span>
    </div>
  </section>

</body>
</html>
```